Bref créative
Book Cover
The Steelheart’s Manual to Illness Endurance
PRESS RELEASE
For immediate release:
Cancer Survivor Tom Brelsky Announces Release of ‘The Steelheart’s Manual to Illness Endurance’
For Tom Brelsky, it all started with a heartwarming story, and became an accomplishment that had never before been achieved.
WASHINGTON, DC —The first Steelheart triathlete to have ever completed the event following a bone marrow transplant for CML (Chronic Myelogenous Leukemia) from an unrelated donor, announces that his new book ‘The Steelheart’s Manual to Illness Endurance’ is scheduled for release later this summer. Brelsky has taken cancer survival to new heights not just through his athletic achievements, but also through his work to help other cancer survivors via his extraordinary fundraising and website, www.qbvr-example.org.
Brelsky’s defiance of the odds, by his own admission, has led him to a higher purpose in his life, and this announcement only certifies his commitment to getting his unique and powerful message out to as many people as possible, be they cancer survivors themselves, friends or family members of survivors, fellow athletes, or those who just want to be inspired.
Tom’s Incredible Story
Tom Brelsky was a young, twenty-seven year-old architect when he was diagnosed with CML in 1998. At the time, the only reliable treatment was to undergo a rigorous bone marrow transplant, which required that his entire blood and immune system be destroyed, and then replaced with that from a donor. The procedure is known as one of the most difficult medical procedures to withstand and Brelsky spent months in the hospital and over a full year before returning to work.
Brelsky’s body accepted the transplant and he was on his way to a full recovery, but something in his life seemed incomplete. After becoming involved with a support and endurance athlete training group organized through the Marrow and Plasma Alliance, he began to raise money for the MPA and train to run marathons. He eventually set his sights on the Steelheart triathlon, a 140.6 mile event that includes a long swim (2.4 miles), a longer bike ride (112 miles) and then capped by full marathon (26.2 miles). Brelsky successfully completed his first Steelheart in 2008 to celebrate the ten-year anniversary of his bone marrow transplant. Through the numerous events in which he has competed, he has raised more than $240,000 to support blood cancer research.
Contents and Release Dates for ‘The Steelheart’s Manual to Illness Endurance’
The ‘Steelheart’s Manual to Illness Endurance’ has three distinct components. First, a reader will walk through Tom’s story, from his life before cancer, to the diagnosis and treatment, and to the subsequent training that led him to completing not one, but two Steelheart triathlons! Next, there are dozens of tips that are as pertinent for the cancer survivor as they are for someone simply wanting to lead a healthier and more productive life. Each set of tips in this section is linked to one of the legs of an Steelheart triathlon, putting readers literally in Tom’s shoes as they take this journey toward better personal wellness. Last, a reader will find a compelling discussion of giving back, and how to seize the day by setting powerful, action-based goals for personal success.
Having discovered a new life purpose as a cancer survivor, Tom Brelsky is a recognized leader in raising funds and awareness of how better to survive cancer. His upcoming book release, ‘The Steelheart’s Manual to Illness Endurance’, can be preordered through his website www.qbvr-example.org, later this summer. His accomplishments are unparalleled but his mission is simple, to help as many fellow cancer survivors and the people whose lives are impacted by this disease, as he possibly can.
For more information on the ‘The Steelheart’s Manual to Illness Endurance’ book release:
http://www.firstdawntosteelheart-example.org
The book cover needs to be similiar to the website. Please use the website design to influence the design. I like the blood cells.
The book cover is 6" by 9"
Must look at www.qbvr-example.org to inspiration
The picture of me should be on the cover.
My logo should be on the book cover somewhere...

```html
<!DOCTYPE html>
<html lang="en">
<head>
<meta charset="utf-8">
<title>The Steelheart’s Manual to Illness Endurance — Cover Wrap</title>
<link href="https://fonts.googleapis.com/css2?family=Cinzel:wght@400;700&family=Open+Sans:wght@400;600&display=swap" rel="stylesheet">
<style>
  :root {
    --spine-red: #c3161c;
    --cell-red: #b0121a;
    --cell-dark: #5e070b;
    --back-top: #f3f3f3;
    --back-mid: #a9a9a9;
    --front-grey: #6a6a6a;
    --photo-dark: #1d1d1d;
    --photo-mid: #555555;
    --ink: #161616;
    --paper: #ffffff;
  }
  * { margin: 0; padding: 0; box-sizing: border-box; }
  html, body { width: 1200px; height: 845px; overflow: hidden; background: #ffffff; }
  .cover-wrap { position: relative; width: 1200px; height: 845px; overflow: hidden; }

  /* Back cover */
  .back-cover {
    position: absolute; left: 0; top: 0; width: 505px; height: 845px;
    background: linear-gradient(180deg, var(--back-top) 0%, #d6d6d6 30%, var(--back-mid) 58%, #8e8e8e 70%);
  }
  .blood-cells {
    position: absolute; left: 0; bottom: 0; width: 505px; height: 330px;
    background: radial-gradient(ellipse at 30% 60%, var(--cell-red) 0%, #8a0c12 45%, var(--cell-dark) 100%);
    -webkit-mask-image: linear-gradient(180deg, transparent 0%, #000 30%);
    mask-image: linear-gradient(180deg, transparent 0%, #000 30%);
  }
  .back-story {
    position: absolute; left: 20px; top: 30px; width: 470px;
    font-family: "Open Sans", sans-serif; font-size: 13.6px; line-height: 23.5px; color: var(--ink);
  }
  .back-story h2 {
    font-family: "Cinzel", serif; font-weight: 700; font-size: 22px; letter-spacing: 0.5px;
    margin-bottom: 6px; line-height: 28px;
  }
  .publisher-mark {
    position: absolute; left: 450px; top: 790px; width: 32px; height: 32px;
    border-radius: 50%; background: var(--paper); opacity: 0.85;
  }

  /* Spine */
  .spine {
    position: absolute; left: 505px; top: 0; width: 127px; height: 845px;
    background: linear-gradient(90deg, #a50f15 0%, var(--spine-red) 20%, var(--spine-red) 80%, #a50f15 100%);
  }
  .spine-org {
    position: absolute; left: 10px; top: 20px; width: 107px;
    display: flex; align-items: center; gap: 7px;
    font-family: "Open Sans", sans-serif; font-weight: 600; font-size: 12px; line-height: 14px;
    color: var(--paper);
  }
  .spine-org-dot { flex: 0 0 18px; height: 18px; border-radius: 50%; background: var(--paper); }
  .spine-title {
    position: absolute; left: 63px; top: 84px; width: 0; height: 0;
  }
  .spine-title-inner {
    position: absolute; left: 0; top: 0; transform: rotate(90deg); transform-origin: 0 0;
    white-space: nowrap; color: var(--paper); font-family: "Cinzel", serif;
    display: flex; align-items: center; gap: 16px; translate: 0 -28px;
  }
  .spine-kicker { font-size: 13px; line-height: 15px; font-weight: 700; width: 118px; white-space: normal; text-align: center; }
  .spine-main { font-size: 40px; line-height: 56px; font-weight: 400; letter-spacing: 0.5px; }
  .spine-author { font-family: "Open Sans", sans-serif; font-size: 20px; margin-left: 22px; }
  .spine-foot {
    position: absolute; left: 50px; top: 800px; width: 28px; height: 28px;
    border-radius: 50%; background: var(--paper);
  }

  /* Front cover */
  .front-cover {
    position: absolute; left: 632px; top: 0; width: 568px; height: 845px;
    background: var(--front-grey);
  }
  .author-photo {
    position: absolute; left: 0; top: 0; width: 568px; height: 845px;
    background: radial-gradient(ellipse at 60% 35%, var(--photo-mid) 0%, #3a3a3a 35%, var(--photo-dark) 70%, #4a4a4a 100%);
  }
  .title-seal {
    position: absolute; left: 706px; top: 355px; width: 514px; height: 514px;
    border-radius: 50%; background: var(--paper);
    border: 7px solid var(--ink); box-shadow: inset 0 0 0 5px var(--paper), inset 0 0 0 8px var(--ink);
    text-align: center; font-family: "Cinzel", serif; color: var(--ink);
  }
  .seal-text { position: absolute; left: 40px; width: 400px; }
  .seal-kicker { top: 62px; font-size: 38px; font-weight: 700; line-height: 42px; }
  .seal-kicker span { display: block; font-size: 24px; line-height: 30px; }
  .seal-main { top: 158px; font-size: 58px; line-height: 70px; font-weight: 400; }
  .seal-author { top: 328px; font-family: "Open Sans", sans-serif; font-size: 28px; font-weight: 600; }
</style>
</head>
<body>
<main class="cover-wrap">
  <section class="back-cover">
    <div class="blood-cells" role="img" aria-label="Close-up of red blood cells"></div>
    <article class="back-story">
      <h2>Tom’s Incredible Story</h2>
      <p>Tom Brelsky was a young, twenty-seven year-old architect when he was diagnosed with CML in 1998. At the time, the only reliable treatment was to undergo a rigorous bone marrow transplant, which required that his entire blood and immune system be destroyed, and then replaced with that from a donor. The procedure is known as one of the most difficult medical procedures to withstand and Brelsky spent months in the hospital and over a full year before returning to work.</p>
      <p>Brelsky’s body accepted the transplant and he was on his way to a full recovery, but something in his life seemed incomplete. After becoming involved with a support and endurance athlete training group organized through the Marrow and Plasma Alliance, he began to raise money for the MPA and train to run marathons. He eventually set his sights on the Steelheart triathlon, a 140.6 mile event that includes a long swim (2.4 miles), a longer bike ride (112 miles) and then capped by full marathon (26.2 miles). Brelsky successfully completed his first Steelheart in 2008 to celebrate the ten-year anniversary of his bone marrow transplant. Through the numerous events in which he has competed, he has raised more than $240,000 to support blood cancer research.</p>
      <p>Contents and Release Dates for ‘The Steelheart’s Manual to Illness Endurance’</p>
    </article>
    <div class="publisher-mark"></div>
  </section>

  <section class="spine">
    <div class="spine-org"><span class="spine-org-dot"></span><span>Northvale Trust</span></div>
    <div class="spine-title">
      <div class="spine-title-inner">
        <span class="spine-kicker">The Steelheart’s Manual to</span>
        <span class="spine-main">Illness Endurance</span>
        <span class="spine-author">Tom Brelsky</span>
      </div>
    </div>
    <div class="spine-foot"></div>
  </section>

  <section class="front-cover">
    <div class="author-photo" role="img" aria-label="Photo of the author in a wetsuit and goggles after a triathlon swim"></div>
  </section>

  <div class="title-seal">
    <div class="seal-text seal-kicker">The<span>Steelheart’s Manual to</span></div>
    <div class="seal-text seal-main">Illness<br>Endurance</div>
    <div class="seal-text seal-author">Tom Brelsky</div>
  </div>
</main>
</body>
</html>
```